"Life's Short. Get a Divorce" - WANTED - Simple, Classy & Sexy Poster!

I am looking for a racy, lacy, sexy, jaw dropping poster to be created that has a picture of a good looking man and woman on either side of the poster which has the slogan 'Life's short. Get a Divorce'. I would also like our company's contact details (along with the services that we offer) to be included in the flyer.

In relation to the images, we would like that show only the bodies of a muscular man and a leggy woman in high heels.

If we could have the woman on one side and the man on the other side (so 2 separate images) with the 'Life's Short. Get a Divorce' in the centre of the page.

Target Market(s)

Mature audience

Requirements
Must have
• A picture of a mature man and woman.
• The slogan 'Life's Short. Get a Divorce' in large bold font.
• Company's header and footer.

```html
<!DOCTYPE html>
<html lang="en">
<head>
<meta charset="utf-8">
<title>Harlow Benning Legal – Life's Short. Get a Divorce</title>
<link rel="stylesheet" href="https://fonts.googleapis.com/css2?family=Poppins:wght@600;700&family=Roboto+Condensed:wght@400&display=swap">
<style>
  :root {
    --backdrop: #2a1a12;
    --band-blue: #19779f;
    --ink: #111111;
    --white: #ffffff;
    --skin-light: #e2c7bd;
    --skin: #c29384;
    --skin-deep: #8f6358;
    --jeans-blue: #3aa6de;
    --splash-pink: #e98bb4;
    --shadow-plum: #5e3a5e;
  }
  html, body {
    margin: 0;
    width: 1200px;
    height: 1200px;
    overflow: hidden;
    background: var(--backdrop);
  }
  .poster {
    position: absolute;
    left: 174px;
    top: 52px;
    width: 852px;
    height: 1096px;
    background: var(--white);
    overflow: hidden;
    font-family: "Roboto Condensed", "Arial Narrow", sans-serif;
  }
  .header-band {
    position: absolute;
    left: 0; top: 0;
    width: 100%;
    height: 152px;
    background: var(--band-blue);
    text-align: center;
    color: var(--white);
  }
  .brand-name {
    position: absolute;
    left: 0; right: 0;
    top: 40px;
    margin: 0;
    font-size: 50px;
    line-height: 1;
    letter-spacing: 2px;
    font-weight: 400;
  }
  .brand-sub {
    position: absolute;
    left: 0; right: 0;
    top: 100px;
    font-size: 26px;
    line-height: 1;
    letter-spacing: 22px;
    font-weight: 400;
    padding-left: 22px;
  }
  .hero-image {
    position: absolute;
    left: 0; top: 152px;
    width: 852px;
    height: 845px;
  }
  .slogan {
    position: absolute;
    left: 0; right: 0;
    top: 446px;
    margin: 0;
    text-align: center;
    font-family: "Poppins", "Helvetica Neue", sans-serif;
    font-weight: 600;
    font-size: 84px;
    line-height: 112px;
    letter-spacing: -3px;
    color: var(--white);
    text-shadow: 4px 5px 6px rgba(0,0,0,0.75);
    padding-left: 40px;
  }
  .services {
    position: absolute;
    left: 0; right: 0;
    top: 896px;
    text-align: center;
    color: var(--ink);
  }
  .services-title {
    margin: 0;
    font-family: "Poppins", "Helvetica Neue", sans-serif;
    font-weight: 700;
    font-size: 33px;
    line-height: 38px;
    letter-spacing: 6px;
  }
  .services-list {
    margin: 2px 0 0;
    font-size: 19px;
    line-height: 24px;
  }
  .footer-band {
    position: absolute;
    left: 0; bottom: 0;
    width: 100%;
    height: 99px;
    background: var(--band-blue);
    color: var(--white);
  }
  .footer-address, .footer-web {
    position: absolute;
    top: 30px;
    font-size: 14.5px;
    line-height: 19px;
  }
  .footer-address { left: 61px; }
  .footer-web { left: 583px; }
  .footer-phone {
    position: absolute;
    left: 377px;
    top: 26px;
    font-size: 28px;
    line-height: 40px;
  }
  .divider {
    position: absolute;
    top: 22px;
    width: 1px;
    height: 44px;
    background: var(--white);
  }
  .divider-left { left: 360px; }
  .divider-right { left: 565px; }
</style>
</head>
<body>
  <main class="poster">
    <header class="header-band">
      <p class="brand-name">HARLOW BENNING</p>
      <div class="brand-sub">LEGAL</div>
    </header>

    <svg class="hero-image" viewBox="0 0 852 845" role="img" aria-label="Photograph of a muscular shirtless man's torso, arms flexed, wearing blue jeans, with blue and pink paint splashes behind him">
      <defs>
        <linearGradient id="subjectTone" x1="0" y1="0" x2="0" y2="1">
          <stop offset="0" stop-color="var(--skin-light)"/>
          <stop offset="0.35" stop-color="var(--skin)"/>
          <stop offset="0.6" stop-color="var(--skin-deep)"/>
          <stop offset="0.68" stop-color="var(--jeans-blue)"/>
          <stop offset="0.92" stop-color="var(--jeans-blue)"/>
          <stop offset="1" stop-color="#ffffff"/>
        </linearGradient>
        <linearGradient id="edgeFade" x1="0" y1="0" x2="1" y2="0">
          <stop offset="0" stop-color="#ffffff" stop-opacity="1"/>
          <stop offset="0.12" stop-color="#ffffff" stop-opacity="0.55"/>
          <stop offset="0.25" stop-color="#ffffff" stop-opacity="0"/>
          <stop offset="0.7" stop-color="var(--shadow-plum)" stop-opacity="0.35"/>
          <stop offset="0.88" stop-color="#ffffff" stop-opacity="0.3"/>
          <stop offset="1" stop-color="#ffffff" stop-opacity="0.85"/>
        </linearGradient>
        <radialGradient id="pinkSplash" cx="0.85" cy="0.8" r="0.32">
          <stop offset="0" stop-color="var(--splash-pink)" stop-opacity="0.9"/>
          <stop offset="1" stop-color="var(--splash-pink)" stop-opacity="0"/>
        </radialGradient>
        <linearGradient id="bottomFade" x1="0" y1="0" x2="0" y2="1">
          <stop offset="0.82" stop-color="#ffffff" stop-opacity="0"/>
          <stop offset="1" stop-color="#ffffff" stop-opacity="0.9"/>
        </linearGradient>
      </defs>
      <rect width="852" height="845" fill="url(#subjectTone)"/>
      <rect width="852" height="845" fill="url(#edgeFade)"/>
      <rect width="852" height="845" fill="url(#pinkSplash)"/>
      <rect width="852" height="845" fill="url(#bottomFade)"/>
    </svg>

    <h1 class="slogan">'LIFE'S SHORT.<br>GET A DIVORCE'</h1>

    <section class="services">
      <h2 class="services-title">SERVICES</h2>
      <p class="services-list">FAMILY LAW &nbsp;|&nbsp; CRIMINAL LAW &nbsp;|&nbsp; TRAFFIC &amp; DRINK DRIVING &nbsp;|&nbsp; COMMERCIAL &amp; PROPERTY LAW<br>CONVEYANCING &nbsp;|&nbsp; WILLS &amp; ESTATES</p>
    </section>

    <footer class="footer-band">
      <div class="footer-address">Level 2/48 Marlow Street<br>Darwin NT 0800, GPO Box 1200 Darwin NT 801</div>
      <span class="divider divider-left"></span>
      <div class="footer-phone">(08) 8900 4517</div>
      <span class="divider divider-right"></span>
      <div class="footer-web">www.harlowbenninglegal.com<br>office@harlowbenninglegal.com</div>
    </footer>
  </main>
</body>
</html>
```